Website design with eCommerce for revolutionary new product in the manufacturing industry.

We need a website designed for a precision manufacturing company based in the suburbs of Minneapolis, Minnesota called Velkor Manufacturing. We have a revolutionary new product, the TRIM LATCH, to introduce and sell through an eCommerce storefront. The website would include company information, product information, and the storefront. Green is a color that represents Velkor Manufacturing. The final design should communicate that we exclusively offer premium products at a premium price. The design should also let the customer know they are the focus of our work.

Target Market(s)

Machinists and machine shops

Industry/Entity Type

Manufacturing and machine shops

Coding

Coded - Design and coding required

Font styles to use
Sans Serif

Colors
59FF00
82FF00
B8FF75
E3FFCB
F4FFEA

Requirements
Must have
• eCommerce storefront, Made in USA references
Nice to have
• Home page, TRIM LATCH Product page, About Us, Capabilities, Contact, etc.
Should not have
• Should not be too much text and reading.

```html
<!DOCTYPE html>
<html lang="en">
<head>
<meta charset="utf-8">
<title>Velkor Manufacturing — TRIM LATCH</title>
<link href="https://fonts.googleapis.com/css2?family=Archivo:ital,wght@0,400;0,500;0,600;0,700;1,400&display=swap" rel="stylesheet">
<style>
:root{
  --green:#35a326;
  --green-bright:#3fb52c;
  --green-soft:#e3ffcb;
  --black:#0b0b0b;
  --ink:#1c1c1c;
  --muted:#4a4a4a;
  --grey-bg:#d9d9d9;
  --white:#ffffff;
}
*{box-sizing:border-box;margin:0;padding:0}
html,body{width:1200px;height:3997px;overflow:hidden;background:var(--white)}
body{font-family:"Archivo",sans-serif;color:var(--ink);position:relative}
.abs{position:absolute}
.btn{position:absolute;display:flex;align-items:center;justify-content:center;font-size:11px;font-weight:600;letter-spacing:.3px;text-transform:uppercase;border-radius:2px}
.btn-green{background:var(--green);color:var(--white)}
.btn-dark{background:var(--black);color:var(--white)}
.h-section{font-size:23px;font-weight:500;letter-spacing:.6px;text-transform:uppercase;color:var(--ink)}
.arrow-bar{position:absolute;display:block}
.placeholder{position:absolute}

/* header */
.site-header{position:absolute;left:0;top:0;width:1200px;height:62px;background:var(--white)}
.brand{position:absolute;left:93px;top:17px;font-size:25px;font-weight:700;letter-spacing:1px;color:var(--black);display:flex;align-items:center;gap:8px}
.brand-dot{width:12px;height:12px;background:var(--green)}
.nav{position:absolute;top:24px;left:452px;display:flex;gap:36px;font-size:11px;font-weight:600;text-transform:uppercase;color:var(--ink)}
.nav .active{color:var(--green)}
.nav-contact{left:906px;top:16px;width:100px;height:31px}
.cart{left:1019px;top:16px;width:88px;height:31px;gap:6px}

/* hero */
.hero{position:absolute;left:0;top:62px;width:1200px;height:469px;background:radial-gradient(ellipse at 60% 40%,#6a6a6a 0%,#3a3a3a 45%,#1d1d1d 100%)}
.hero-kicker{left:200px;top:116px;color:var(--white);font-size:15px;font-weight:500;letter-spacing:.4px}
.hero-title{left:200px;top:150px;width:520px;color:var(--white);font-size:31px;font-weight:500;line-height:36px;letter-spacing:.5px;text-transform:uppercase}
.hero-btn{left:200px;top:320px;width:100px;height:30px}

/* why */
.why-title{left:613px;top:642px}
.why-lead{left:613px;top:680px;width:390px;font-size:11px;line-height:15px;color:var(--muted)}
.ticks{position:absolute;list-style:none;font-size:12px;color:var(--ink)}
.ticks li{position:relative;padding-left:22px;margin-bottom:6px;line-height:16px}
.ticks li svg{position:absolute;left:0;top:3px}
.why-ticks{left:613px;top:724px}
.why-btn{left:613px;top:806px;width:100px;height:31px}
.divider-shadow{position:absolute;left:0;top:955px;width:1200px;height:10px;background:linear-gradient(#e6e6e6,rgba(255,255,255,0))}

/* capabilities */
.cap-title{left:0;top:1014px;width:1200px;text-align:center}
.cap-sub{left:0;top:1052px;width:1200px;text-align:center;font-size:12px;line-height:16px;color:var(--ink)}
.cap-card{position:absolute;top:1094px;width:275px;height:194px;padding:14px 16px}
.cap-card + .cap-card{border-left:1px solid #e2e2e2}
.cap-card h3{margin-top:46px;font-size:15px;font-weight:500;color:var(--ink)}
.cap-card p{margin-top:10px;font-size:9.5px;line-height:12.5px;color:var(--muted)}
.learn{margin-top:14px;display:flex;align-items:center;gap:6px;font-size:8.5px;font-weight:700;color:var(--green);text-transform:uppercase}
.chev{position:absolute;top:1214px}

/* products */
.products{position:absolute;left:0;top:1368px;width:1200px;height:448px;background:linear-gradient(135deg,#dcdcdc,#c8c8c8 50%,#dcdcdc)}
.prod-title{left:0;top:1420px;width:1200px;text-align:center}
.prod-card{position:absolute;top:1490px;width:205px;height:189px;background:var(--white)}
.prod-frame{position:absolute;left:14px;top:14px;width:160px;height:160px;border:2px solid var(--green)}
.prod-tag{position:absolute;left:12px;top:82px;padding:4px 12px;background:var(--green);color:var(--white);font-size:11px;font-weight:600;border-radius:0 12px 12px 0}
.prod-btn{left:551px;top:1721px;width:98px;height:30px}

/* what we do */
.wwd-title{left:200px;top:1934px}
.wwd-text{left:200px;top:1975px;width:460px;font-size:10.5px;line-height:15px;color:var(--ink)}
.wwd-text p{margin-bottom:15px}
.wwd-btn{left:200px;top:2177px;width:100px;height:31px}

/* wisdom */
.wisdom{position:absolute;left:0;top:2336px;width:1200px;height:282px;background:linear-gradient(120deg,#3aa92b,#2e9a22 50%,#3ab02a)}
.wis-title{left:0;top:2388px;width:1200px;text-align:center;color:var(--white)}
.wis-quote{left:0;top:2438px;width:1200px;text-align:center;color:var(--white);font-size:29px;font-style:italic}
.wis-src{left:0;top:2482px;width:1200px;text-align:center;color:var(--white);font-size:13px}
.wis-dot{position:absolute;top:2529px;width:24px;height:24px;border:1px solid rgba(255,255,255,.8);border-radius:50%}

/* gallery */
.gal-title{left:0;top:2670px;width:1200px;text-align:center}
.gal-btn{left:551px;top:3155px;width:98px;height:31px}
.section-end{position:absolute;left:0;top:3251px;width:1200px;height:10px;background:linear-gradient(#e9e9e9,rgba(255,255,255,0))}

/* better */
.better-title{left:242px;top:3312px}
.better-list{left:613px;top:3320px;width:385px;font-size:10.5px}
.better-list li{margin-bottom:10px;line-height:14px}
.better-btn{left:613px;top:3579px;width:100px;height:31px}

/* footer */
.site-footer{position:absolute;left:0;top:3675px;width:1200px;height:322px;background:var(--black);color:var(--white)}
.foot-brand{left:200px;top:58px;font-size:27px;font-weight:700;letter-spacing:1px;display:flex;align-items:center;gap:8px}
.foot-sub{left:238px;top:116px;font-size:22px;font-weight:600;letter-spacing:1px}
.foot-h{font-size:11px;font-weight:600;letter-spacing:.5px;text-transform:uppercase}
.foot-call{left:475px;top:78px;font-size:17px;color:var(--green-bright)}
.foot-mail{left:475px;top:100px;font-size:12px}
.foot-label{font-size:9px;color:var(--green-bright);text-transform:uppercase;font-weight:600}
.foot-addr{left:475px;top:143px;font-size:12px;line-height:15px;width:200px}
.social{position:absolute;top:227px;width:29px;height:29px;border-radius:50%;background:#e6e6e6}
.social.on{background:var(--green-bright)}
.field{position:absolute;background:#f2f2f2;color:#555;font-size:9px;padding:7px 8px}
.send{left:718px;top:227px;width:88px;height:31px}
.foot-rule{position:absolute;left:200px;top:278px;width:800px;height:1px;background:#333}
.copy{left:200px;top:292px;font-size:10px}
.copy span{color:var(--green-bright)}
.foot-nav{position:absolute;left:487px;top:292px;display:flex;gap:28px;font-size:10px}
.foot-nav .active{color:var(--green-bright)}
</style>
</head>
<body>

<header class="site-header">
  <div class="brand"><span class="brand-dot"></span>TRIM LATCH</div>
  <nav class="nav">
    <span class="active">– Home –</span><span>Capabilities</span><span>About Us</span><span>Gallery</span><span>Wisdom</span>
  </nav>
  <div class="btn btn-dark nav-contact">Contact Us</div>
  <div class="btn btn-green cart">
    <svg width="12" height="11" viewBox="0 0 12 11"><path d="M0 1h2l2 6h6l1.5-4.5H3" fill="none" stroke="#fff" stroke-width="1.3"/><circle cx="5" cy="9.5" r="1" fill="#fff"/><circle cx="9" cy="9.5" r="1" fill="#fff"/></svg>$0.00
  </div>
</header>

<section class="hero" aria-label="Hero">
  <div class="placeholder" role="img" aria-label="Green TRIM LATCH product render" style="left:714px;top:62px;width:264px;height:342px;background:linear-gradient(150deg,#3dbb2b,#1f7a16);border-radius:6px;opacity:.9"></div>
</section>
<svg class="arrow-bar" style="left:404px;top:48px" width="796" height="30" viewBox="0 0 796 30"><polygon points="0,15 18,0 18,10 796,10 796,20 18,20 18,30" fill="var(--green)"/></svg>
<div class="abs hero-kicker">WELCOME TO VELKOR MANUFACTURING</div>
<h1 class="abs hero-title">We are a machine shop with complete end to end manufacturing capabilities.</h1>
<div class="btn btn-green hero-btn">About Us</div>
<svg class="arrow-bar" style="left:0;top:521px" width="794" height="30" viewBox="0 0 794 30"><polygon points="0,10 776,10 776,0 794,15 776,30 776,20 0,20" fill="var(--green)"/></svg>

<section aria-label="Why Velkor">
  <div class="placeholder" role="img" aria-label="Photo of TRIM LATCH in foam case" style="left:200px;top:610px;width:149px;height:119px;background:linear-gradient(135deg,#3a3a3a,#5d5d5d)"></div>
  <div class="placeholder" role="img" aria-label="Photo of TRIM LATCH parts in case" style="left:200px;top:754px;width:149px;height:118px;background:linear-gradient(135deg,#4a4a4a,#2f2f2f)"></div>
  <div class="placeholder" role="img" aria-label="TRIM LATCH product illustration" style="left:349px;top:590px;width:225px;height:302px;background:linear-gradient(150deg,#44bf30,#1f7a16);border-radius:6px"></div>
  <h2 class="abs h-section why-title">Why Velkor Manufacturing?</h2>
  <p class="abs why-lead">Because there is a better way, and we will find it, even if it's the hard way. We believe in working harder and smarter to achieve success.</p>
  <ul class="ticks why-ticks">
    <li><svg width="10" height="8" viewBox="0 0 10 8"><path d="M0 4h8M5 1l3 3-3 3" fill="none" stroke="var(--green)" stroke-width="1.2"/></svg>Our success is measured in your success</li>
    <li><svg width="10" height="8" viewBox="0 0 10 8"><path d="M0 4h8M5 1l3 3-3 3" fill="none" stroke="var(--green)" stroke-width="1.2"/></svg>Focused on your needs and making excellent parts</li>
    <li><svg width="10" height="8" viewBox="0 0 10 8"><path d="M0 4h8M5 1l3 3-3 3" fill="none" stroke="var(--green)" stroke-width="1.2"/></svg>Exceeding your expectations</li>
  </ul>
  <div class="btn btn-dark why-btn">Contact Us</div>
</section>
<div class="divider-shadow"></div>

<section aria-label="Capabilities">
  <h2 class="abs h-section cap-title">Capabilities</h2>
  <p class="abs cap-sub">While this list covers much of our capabilities, it is by no means exhaustive.<br>You can always contact us with specific requests.</p>
  <svg class="chev" style="left:140px" width="12" height="20" viewBox="0 0 12 20"><path d="M10 2L2 10l8 8" fill="none" stroke="#222" stroke-width="1.6"/></svg>
  <svg class="chev" style="left:1048px" width="12" height="20" viewBox="0 0 12 20"><path d="M2 2l8 8-8 8" fill="none" stroke="#222" stroke-width="1.6"/></svg>
  <article class="cap-card" style="left:200px">
    <svg class="abs" style="left:16px;top:12px" width="46" height="32" viewBox="0 0 46 32"><path d="M2 30L10 2l8 28 8-28 8 28 8-28" fill="none" stroke="var(--green)" stroke-width="2.5"/></svg>
    <h3>CAD Design</h3>
    <p>Do you have something that needs to be created, but no method of capturing the design? We use current 3D CAD modeling software to bring your ideas to life ...</p>
    <div class="learn">Learn more <svg width="10" height="10"><circle cx="5" cy="5" r="4" fill="none" stroke="var(--green)"/></svg></div>
  </article>
  <article class="cap-card" style="left:475px">
    <svg class="abs" style="left:16px;top:12px" width="40" height="32" viewBox="0 0 40 32"><circle cx="14" cy="18" r="9" fill="none" stroke="var(--green)" stroke-width="5" stroke-dasharray="4 3"/><circle cx="30" cy="9" r="6" fill="none" stroke="var(--green)" stroke-width="4" stroke-dasharray="3 2"/></svg>
    <h3>CAM Programming</h3>
    <p>Do you need programs for your machines? Perhaps we can help. We use current 3D CAM programming software to take your designs to code that a CNC machine can use ...</p>
    <div class="learn">Learn more <svg width="10" height="10"><circle cx="5" cy="5" r="4" fill="none" stroke="var(--green)"/></svg></div>
  </article>
  <article class="cap-card" style="left:750px">
    <svg class="abs" style="left:16px;top:12px" width="36" height="32" viewBox="0 0 36 32"><path d="M4 10h20v20H4zM4 10l8-8h20v20l-8 8M24 10l8-8" fill="none" stroke="var(--green)" stroke-width="2.5"/></svg>
    <h3>FFF 3D Printing</h3>
    <p>Do you need a quick sample? Using Fused Filament Fabrication we can 3D print prototypes for evaluation, or fully functioning end use products ...</p>
    <div class="learn">Learn more <svg width="10" height="10"><circle cx="5" cy="5" r="4" fill="none" stroke="var(--green)"/></svg></div>
  </article>
</section>

<section class="products" aria-label="Our products"></section>
<svg class="arrow-bar" style="left:404px;top:1350px" width="796" height="30" viewBox="0 0 796 30"><polygon points="0,15 18,0 18,10 796,10 796,20 18,20 18,30" fill="var(--green)"/></svg>
<h2 class="abs h-section prod-title">Our Products</h2>
<div class="prod-card" style="left:200px"><div class="prod-frame"></div><div class="placeholder" role="img" aria-label="TRIM LATCH model TL-101 render" style="left:95px;top:-6px;width:155px;height:200px;background:linear-gradient(150deg,#44bf30,#1f7a16);border-radius:6px"></div><div class="prod-tag">TL-101</div></div>
<div class="prod-card" style="left:475px"><div class="prod-frame"></div><div class="placeholder" role="img" aria-label="TRIM LATCH model TL-102 render" style="left:95px;top:-6px;width:155px;height:200px;background:linear-gradient(150deg,#44bf30,#1f7a16);border-radius:6px"></div><div class="prod-tag">TL-102</div></div>
<div class="prod-card" style="left:750px"><div class="prod-frame"></div><div class="placeholder" role="img" aria-label="TRIM LATCH model TL-103 render" style="left:95px;top:-6px;width:155px;height:200px;background:linear-gradient(150deg,#44bf30,#1f7a16);border-radius:6px"></div><div class="prod-tag">TL-103</div></div>
<div class="btn btn-dark prod-btn">Shop Now!</div>
<svg class="arrow-bar" style="left:0;top:1800px" width="794" height="30" viewBox="0 0 794 30"><polygon points="0,10 776,10 776,0 794,15 776,30 776,20 0,20" fill="var(--green)"/></svg>

<section aria-label="What we do">
  <h2 class="abs h-section wwd-title">What We Do</h2>
  <div class="abs wwd-text">
    <p>We are a machine shop with complete end to end manufacturing capabilities. We can take an idea or need, and bring it to a complete physical product. We can design and build your prototype, and we can mass produce it too.</p>
    <p>We love working directly with customers to manufacture their products, and help make it better where appropriate. We can work with as little as a verbal description, up to following fully defined customer specifications.</p>
    <p>We work in a wide variety of materials, and are very good at creating fixture designs to address your process issues. We can even come to your business and help you make improvements onsite. We have helped many other machine shops be more successful.</p>
  </div>
  <div class="btn btn-green wwd-btn">Contact Us</div>
  <div class="placeholder" role="img" aria-label="Photo of rows of machined aluminium parts" style="left:712px;top:1876px;width:288px;height:395px;background:linear-gradient(160deg,#8d8d8d,#4e4e4e 50%,#9a9a9a)"></div>
</section>

<section class="wisdom" aria-label="Words of wisdom"></section>
<svg class="arrow-bar" style="left:404px;top:2319px" width="796" height="30" viewBox="0 0 796 30"><polygon points="0,15 18,0 18,10 796,10 796,20 18,20 18,30" fill="var(--black)"/></svg>
<h2 class="abs h-section wis-title">Words of Wisdom</h2>
<p class="abs wis-quote">“Sometimes the shortcut is the long way.”</p>
<p class="abs wis-src">- Japanese Wisdom -</p>
<div class="wis-dot" style="left:572px"><svg width="22" height="22"><path d="M13 7l-4 4 4 4" fill="none" stroke="#fff" stroke-width="1.2"/></svg></div>
<div class="wis-dot" style="left:603px"><svg width="22" height="22"><path d="M9 7l4 4-4 4" fill="none" stroke="#fff" stroke-width="1.2"/></svg></div>
<svg class="arrow-bar" style="left:0;top:2603px" width="794" height="30" viewBox="0 0 794 30"><polygon points="0,10 776,10 776,0 794,15 776,30 776,20 0,20" fill="var(--black)"/></svg>

<section aria-label="Photo gallery">
  <h2 class="abs h-section gal-title">Photo Gallery</h2>
  <div class="placeholder" role="img" aria-label="Photo of machined nuts on wood" style="left:200px;top:2724px;width:250px;height:188px;background:linear-gradient(135deg,#b8a78a,#8a8a8a)"></div>
  <div class="placeholder" role="img" aria-label="Photo of pin array on metal plate" style="left:475px;top:2724px;width:250px;height:400px;background:linear-gradient(160deg,#9a9a9a,#4a4a4a 55%,#7d7d7d)"></div>
  <div class="placeholder" role="img" aria-label="Photo of bronze parts on blue mat" style="left:750px;top:2724px;width:250px;height:188px;background:linear-gradient(135deg,#2f5ea8,#a67a4a 60%,#2f5ea8)"></div>
  <div class="placeholder" role="img" aria-label="Photo of a triangular machined part" style="left:200px;top:2936px;width:250px;height:188px;background:linear-gradient(135deg,#3c3c3c,#a0a0a0 50%,#333)"></div>
  <div class="placeholder" role="img" aria-label="Photo of perforated metal disc" style="left:750px;top:2936px;width:250px;height:188px;background:radial-gradient(circle at 45% 40%,#c8c8c8,#6a6a6a 70%)"></div>
  <div class="btn btn-green gal-btn">View All</div>
</section>
<div class="section-end"></div>

<section aria-label="How we make it better">
  <h2 class="abs h-section better-title">How We Make It Better</h2>
  <div class="placeholder" role="img" aria-label="TRIM LATCH product illustration" style="left:280px;top:3370px;width:230px;height:200px;background:linear-gradient(150deg,#44bf30,#1f7a16);border-radius:6px"></div>
  <ul class="ticks better-list">
    <li><svg width="10" height="8" viewBox="0 0 10 8"><path d="M0 4h8M5 1l3 3-3 3" fill="none" stroke="var(--green)" stroke-width="1.2"/></svg>With 100 years of combined knowledge and experience to draw upon, we find solutions.</li>
    <li><svg width="10" height="8" viewBox="0 0 10 8"><path d="M0 4h8M5 1l3 3-3 3" fill="none" stroke="var(--green)" stroke-width="1.2"/></svg>Our vast experience across multiple industries gives us insight that is invaluable in creativity and foresight.</li>
    <li><svg width="10" height="8" viewBox="0 0 10 8"><path d="M0 4h8M5 1l3 3-3 3" fill="none" stroke="var(--green)" stroke-width="1.2"/></svg>This real life experience brings a broader understanding of what works, and more importantly, what doesn't work, ultimately allowing us to make more informed decisions.</li>
    <li><svg width="10" height="8" viewBox="0 0 10 8"><path d="M0 4h8M5 1l3 3-3 3" fill="none" stroke="var(--green)" stroke-width="1.2"/></svg>We consider the smallest details, and envision all the consequences in order to create a better product the first time.</li>
    <li><svg width="10" height="8" viewBox="0 0 10 8"><path d="M0 4h8M5 1l3 3-3 3" fill="none" stroke="var(--green)" stroke-width="1.2"/></svg>By recognizing risks early, we can address them before they become issues.</li>
    <li><svg width="10" height="8" viewBox="0 0 10 8"><path d="M0 4h8M5 1l3 3-3 3" fill="none" stroke="var(--green)" stroke-width="1.2"/></svg>We continuously improve and learn new things by staying up to date with emerging technologies and techniques.</li>
  </ul>
  <div class="btn btn-dark better-btn">Contact Us</div>
</section>

<footer class="site-footer">
  <div class="abs foot-brand"><span class="brand-dot"></span>TRIM LATCH</div>
  <div class="abs foot-sub">VELKOR MFG</div>
  <div class="abs foot-h" style="left:475px;top:52px">Contact Us</div>
  <div class="abs foot-call">Call: 555-014-2288</div>
  <div class="abs foot-mail">hello@velkormfg.com</div>
  <div class="abs foot-label" style="left:475px;top:130px">Address:</div>
  <div class="abs foot-addr">4820 Alder Works Way, Suite 12<br>Maple Grove, MN</div>
  <div class="abs foot-label" style="left:475px;top:208px">Follow Us</div>
  <div class="social" style="left:475px"></div>
  <div class="social on" style="left:513px"></div>
  <div class="social" style="left:550px"></div>
  <div class="abs foot-h" style="left:718px;top:52px">Send Us Message</div>
  <div class="field" style="left:718px;top:75px;width:135px;height:24px">Name</div>
  <div class="field" style="left:865px;top:75px;width:135px;height:24px">Phone</div>
  <div class="field" style="left:718px;top:112px;width:282px;height:24px">Email</div>
  <div class="field" style="left:718px;top:150px;width:282px;height:58px">Message</div>
  <div class="btn btn-green send">Send</div>
  <svg class="abs" style="left:1025px;top:248px" width="18" height="22" viewBox="0 0 18 22"><path d="M9 2L2 20M9 2l7 18M5 12h8" fill="none" stroke="var(--green-bright)" stroke-width="1.6"/></svg>
  <div class="foot-rule"></div>
  <div class="abs copy">© 2022 <span>TRIM LATCH</span>. All Right Reserved</div>
  <nav class="foot-nav"><span class="active">– Home –</span><span>Capabilities</span><span>About Us</span><span>Gallery</span><span>Wisdom</span><span>Contact Us</span></nav>
</footer>
<svg class="arrow-bar" style="left:404px;top:3660px" width="796" height="30" viewBox="0 0 796 30"><polygon points="0,15 18,0 18,10 796,10 796,20 18,20 18,30" fill="var(--green)"/></svg>

</body>
</html>
```